Brookside Grocer

Hope all is well!

Wanted to make business cards for my father. His name is Hamid Surani and owns convenience stores. I have attached logo :)

He does not want any title just simple name and phone. An email would be nice as well.

Hamid Surani
Cell: 413-585-2046
Store: 413-719-4820

Brooksidegrocer512@fernpost.com

The design and style is totally up to you :) The colors we were looking for were the same as logo :)

```html
<!DOCTYPE html>
<html lang="en">
<head>
<meta charset="utf-8">
<title>Brookside Grocer — Business Card</title>
<link rel="stylesheet" href="https://fonts.googleapis.com/css2?family=Poppins:wght@400;500;600;700&display=swap">
<style>
  :root {
    --navy: #263a7a;
    --red: #ec2f38;
    --paper: #ffffff;
    --page: #ffffff;
  }
  * { box-sizing: border-box; margin: 0; padding: 0; }
  html, body {
    width: 942px; height: 1200px; overflow: hidden;
    background: var(--page);
    font-family: "Poppins", sans-serif;
  }
  .sheet { position: relative; width: 942px; height: 1200px; }
  .card {
    position: absolute; left: 126px; width: 692px; height: 424px;
    background: var(--paper);
    box-shadow: 0 4px 14px rgba(0,0,0,0.10);
    overflow: hidden;
  }
  .card--front { top: 123px; }
  .card--back { top: 656px; }

  .bar { position: absolute; }
  .bar--thin-navy { height: 1.5px; background: var(--navy); }
  .bar--rule-navy { height: 2.5px; background: var(--navy); }
  .bar--red { background: var(--red); }
  .bar--navy { background: var(--navy); }

  .holder-name {
    position: absolute; left: 39px; top: 71px;
    font-weight: 500; font-size: 39px; line-height: 1;
    color: var(--navy); letter-spacing: 0.2px; white-space: nowrap;
  }

  .brand {
    position: absolute; color: var(--navy);
    font-weight: 700; white-space: nowrap; line-height: 1;
  }
  .card--front .brand { left: 39px; top: 254px; font-size: 25px; }
  .card--back .brand {
    left: 0; right: 0; top: 168px; text-align: center; font-size: 44px;
  }

  .contacts { position: absolute; left: 355px; top: 207px; list-style: none; }
  .contact {
    display: flex; align-items: center; height: 27px; margin-bottom: 9.5px;
    color: var(--navy); white-space: nowrap;
  }
  .contact__icon { width: 28px; height: 28px; margin-right: 9px; flex: none; }
  .contact__text { font-size: 19px; font-weight: 600; letter-spacing: 0.2px; }
  .contact__text--email { font-size: 15.5px; font-weight: 500; letter-spacing: 0; }
</style>
</head>
<body>
<main class="sheet">

  <section class="card card--front">
    <div class="bar bar--thin-navy" style="left:0;width:34px;top:63px"></div>
    <div class="bar bar--thin-navy" style="left:0;width:34px;top:68px"></div>
    <div class="bar bar--thin-navy" style="left:0;width:34px;top:73px"></div>
    <div class="bar bar--red" style="left:0;width:34px;top:81px;height:20px"></div>
    <div class="bar bar--navy" style="left:0;width:34px;top:105px;height:10px"></div>
    <div class="bar bar--thin-navy" style="left:356px;right:0;top:63px"></div>
    <div class="bar bar--thin-navy" style="left:356px;right:0;top:68px"></div>
    <div class="bar bar--thin-navy" style="left:356px;right:0;top:73px"></div>
    <div class="bar bar--red" style="left:356px;right:0;top:81px;height:20px"></div>
    <div class="bar bar--navy" style="left:356px;right:0;top:105px;height:10px"></div>

    <h1 class="holder-name">HAMID SURANI</h1>

    <p class="brand">Brookside Grocer</p>

    <ul class="contacts">
      <li class="contact">
        <svg class="contact__icon" viewBox="0 0 28 28" aria-hidden="true">
          <circle cx="14" cy="14" r="13" fill="none" stroke="#ec2f38" stroke-width="1.2"/>
          <circle cx="14" cy="14" r="10.5" fill="#ec2f38"/>
          <path d="M10 8.5c.6-.4 1.3-.3 1.6.3l1 1.8c.3.5.1 1-.3 1.3l-.7.5c.5 1.4 1.6 2.6 3 3.2l.5-.7c.3-.4.9-.5 1.3-.3l1.8 1c.6.3.7 1 .3 1.5-.9 1.1-2.3 1.4-3.6.8-2.6-1.2-4.5-3.3-5.5-5.9-.4-1.2 0-2.5 1-3.3z" fill="#fff"/>
        </svg>
        <span class="contact__text">413-585-2046</span>
      </li>
      <li class="contact">
        <svg class="contact__icon" viewBox="0 0 28 28" aria-hidden="true">
          <circle cx="14" cy="14" r="13" fill="none" stroke="#ec2f38" stroke-width="1.2"/>
          <circle cx="14" cy="14" r="10.5" fill="#ec2f38"/>
          <path d="M14 7.5l6.5 5.6h-1.8v6.4h-9.4v-6.4H7.5z" fill="#fff"/>
          <rect x="12.6" y="15.5" width="2.8" height="4" fill="#ec2f38"/>
        </svg>
        <span class="contact__text">413-719-4820</span>
      </li>
      <li class="contact">
        <svg class="contact__icon" viewBox="0 0 28 28" aria-hidden="true">
          <circle cx="14" cy="14" r="13" fill="none" stroke="#ec2f38" stroke-width="1.2"/>
          <circle cx="14" cy="14" r="10.5" fill="#ec2f38"/>
          <rect x="8" y="10" width="12" height="8.5" fill="#fff"/>
          <path d="M8 10l6 5 6-5M8 18.5l4.5-4.5M20 18.5l-4.5-4.5" fill="none" stroke="#ec2f38" stroke-width="1"/>
        </svg>
        <span class="contact__text contact__text--email">Brooksidegrocer512@fernpost.com</span>
      </li>
    </ul>

    <div class="bar bar--rule-navy" style="left:0;right:0;top:373px"></div>
    <div class="bar bar--rule-navy" style="left:0;right:0;top:381px"></div>
    <div class="bar bar--rule-navy" style="left:0;right:0;top:389px"></div>
    <div class="bar bar--red" style="left:0;right:0;top:396px;height:28px"></div>
  </section>

  <section class="card card--back">
    <p class="brand">Brookside Grocer</p>

    <div class="bar bar--rule-navy" style="left:0;right:0;top:352px"></div>
    <div class="bar bar--rule-navy" style="left:0;right:0;top:361px"></div>
    <div class="bar bar--rule-navy" style="left:0;right:0;top:371px"></div>
    <div class="bar bar--red" style="left:0;right:0;top:381px;height:43px"></div>
  </section>

</main>
</body>
</html>
```